Campaign Website

I need a website for my judicial campaign. I would like a site that directs from this domain as well as a new domain with my married last name. I need separate pages on the site that address my diversion programs, and a page to allow people to donate with a link to my bank account and a link for people to submit requests to volunteer, get yard signs, etc.

```html
<!DOCTYPE html>
<html lang="en">
<head>
<meta charset="utf-8">
<title>Judge Harper Loretta — Campaign</title>
<link rel="stylesheet" href="https://fonts.googleapis.com/css2?family=Lato:ital,wght@0,400;0,700;0,900;1,400&display=swap">
<style>
:root{
  --navy:#0d1e3d;
  --navy-deep:#081329;
  --blue:#1a9bd7;
  --blue-dark:#1482b8;
  --orange:#ff6a0d;
  --grey-bg:#ececec;
  --ink:#1d1d1d;
  --text:#333;
  --muted:#666;
  --white:#fff;
}
*{box-sizing:border-box;margin:0;padding:0}
html,body{width:1200px;height:4508px;overflow:hidden}
body{position:relative;font-family:'Lato',sans-serif;color:var(--text);background:var(--white)}
.abs{position:absolute}

/* hero */
.hero{left:0;top:0;width:1200px;height:780px;overflow:hidden;background:linear-gradient(180deg,#0a1a38 0%,#12305a 55%,#1a3c66 100%)}
.hero-scene{left:0;top:0;width:1200px;height:780px;background:radial-gradient(ellipse at 45% 40%,rgba(140,170,210,.35),transparent 55%),linear-gradient(180deg,transparent 60%,rgba(40,90,140,.6) 90%)}
.hero-portrait{left:545px;top:140px;width:600px;height:600px;border-radius:46% 46% 0 0;background:linear-gradient(180deg,#3a2a25 0%,#1b1512 35%,#0e0c0c 100%)}
.brand{left:142px;top:46px;color:var(--white);font-weight:900;font-size:31px;line-height:32px;letter-spacing:1px}
.call{left:640px;top:36px;color:var(--white);font-size:23px;display:flex;align-items:center;gap:10px}
.call b{font-weight:700}
.btn{display:inline-block;background:var(--orange);color:var(--white);font-weight:700;text-transform:uppercase;text-align:center}
.donate-top{left:912px;top:30px;width:144px;height:42px;line-height:42px;font-size:14px}
.nav{left:382px;top:96px;display:flex;gap:20px;font-size:14px;font-weight:900;color:var(--white);text-transform:uppercase}
.nav .active{color:var(--orange)}
.hero-title{left:142px;top:238px;color:var(--white);font-weight:900;font-size:56px;line-height:64px;text-transform:uppercase}
.read-more{left:142px;top:456px;width:160px;height:42px;line-height:42px;font-size:15px}
.arrow{width:30px;height:30px;border-radius:50%;background:rgba(0,0,0,.55)}
.hero-wave{left:0;top:600px;width:1200px;height:180px}

/* about */
.about-photo{left:141px;top:780px;width:400px;height:400px;border-radius:50%;border:7px solid var(--blue);background:linear-gradient(135deg,#5b6c86 0%,#c8b7a4 45%,#5d4b3c 100%)}
.about-kicker{left:582px;top:778px;color:var(--blue);font-size:38px;font-weight:400}
.about-name{left:582px;top:820px;color:var(--ink);font-size:38px;font-weight:700}
.about-text{left:582px;top:880px;width:480px;font-size:14px;line-height:30.5px;color:var(--text)}
.about-btn{left:582px;top:1146px;width:124px;height:38px;line-height:38px;font-size:13px;background:var(--blue);border-radius:3px;box-shadow:0 2px 4px rgba(0,0,0,.2)}

/* thanks band */
.band{left:0;top:1275px;width:1200px;height:665px;background:var(--grey-bg)}
.thanks{left:0;top:1357px;width:1200px;text-align:center;color:var(--ink);font-size:24px;line-height:45px;text-transform:uppercase}
.thanks b{font-weight:700}
.feature{top:1536px;width:270px;text-align:center}
.feature .icon{width:112px;height:112px;border-radius:50%;background:var(--orange);margin:0 auto;display:flex;align-items:center;justify-content:center}
.feature h3{margin-top:24px;font-size:17px;font-weight:900;color:var(--ink);text-transform:uppercase}
.feature p{margin-top:14px;font-size:13.5px;line-height:26px;color:var(--text)}

/* campaign */
.section-title{left:0;width:1200px;text-align:center;color:var(--ink);font-weight:900;font-size:37px;text-transform:uppercase;letter-spacing:-.5px}
.lower-band{left:0;top:2345px;width:1200px;height:845px;background:var(--grey-bg)}
.video{left:145px;top:2120px;width:905px;height:445px;border:4px solid var(--white);box-shadow:0 2px 10px rgba(0,0,0,.25);background:linear-gradient(180deg,#2b2a6e 0%,#7a4a8e 35%,#2a4a7a 60%,#1c1a20 100%)}
.play{left:555px;top:2300px;width:84px;height:46px;border-radius:10px;background:#e21b1b;display:flex;align-items:center;justify-content:center}

/* blog */
.post-main{left:142px;top:2733px;width:428px;height:364px;background:linear-gradient(135deg,#3d6f9b 0%,#a9c2d8 45%,#3a2c26 100%)}
.post-overlay{left:220px;top:2925px;width:350px;height:172px;background:rgba(26,155,215,.95);color:var(--white);padding:24px 22px}
.post-overlay h4{font-size:18px;font-weight:400;line-height:26px}
.meta{font-size:13px;font-style:italic;display:flex;gap:14px;align-items:center;margin-top:12px}
.post-overlay .meta{color:var(--white)}
.post-overlay p{font-size:13px;line-height:20px;margin-top:12px}
.post{left:602px;width:451px;height:172px;background:var(--white);box-shadow:0 1px 4px rgba(0,0,0,.12);display:flex}
.post .thumb{width:190px;height:172px}
.post .body{padding:22px 22px}
.post h4{font-size:18px;font-weight:400;color:var(--ink)}
.post .meta{color:var(--blue);margin-top:10px}
.post p{font-size:13px;line-height:21px;color:var(--text);margin-top:10px}
.sep{width:1px;height:16px;background:var(--muted)}

/* testimonials */
.quote{top:3338px;width:277px;height:170px;background:var(--white);box-shadow:0 1px 6px rgba(0,0,0,.14);padding:18px 18px}
.stars{display:flex;gap:3px}
.quote p{margin-top:14px;font-size:13px;line-height:24px;color:var(--text)}
.quote p span{color:#bbb;font-weight:900;font-size:20px;margin-right:10px}
.author{top:3525px;display:flex;align-items:center;gap:12px}
.avatar{width:60px;height:60px;border-radius:50%;background:linear-gradient(135deg,#cfd6df,#8c98a6)}
.author .name{font-size:13px;color:var(--blue)}
.author .date{font-size:13px;color:var(--text);margin-top:8px}
.dots{left:0;top:3634px;width:1200px;display:flex;justify-content:center;align-items:center;gap:12px}
.dots i{display:block;width:6px;height:6px;border-radius:50%;background:var(--ink)}
.dots i.on{width:12px;height:12px}

/* contact */
.contact{left:0;top:3620px;width:1200px;height:680px}
.contact-bg{left:0;top:3720px;width:1200px;height:580px;background:linear-gradient(180deg,var(--blue) 0%,var(--blue-dark) 100%)}
.contact-title{top:3815px;color:var(--white)}
.info{top:3897px;display:flex;gap:16px;color:var(--white);font-size:18px;line-height:27px}
.info .ic{width:42px;height:42px;border-radius:50%;border:2px solid var(--white);display:flex;align-items:center;justify-content:center;flex:none;margin-top:6px}
.info b{font-weight:700}
.field{border:1px solid rgba(255,255,255,.8);color:var(--white);font-size:12px;padding:0 12px;display:flex;align-items:center}
.field.area{align-items:flex-start;padding-top:14px}
.submit{left:510px;top:4190px;width:178px;height:42px;line-height:42px;font-size:18px}

/* footer */
.footer-text{left:0;top:4356px;width:1200px;text-align:center;font-size:16px;color:var(--ink)}
.social{top:4408px;width:36px;height:36px;border-radius:50%;border:1.5px solid var(--ink)}
</style>
</head>
<body>

<!-- Hero -->
<section class="abs hero">
  <div class="abs hero-scene" role="img" aria-label="Night view of a white cable-stayed bridge arch over a lit city skyline"></div>
  <div class="abs hero-portrait" role="img" aria-label="Portrait of the judge in a black robe with a pearl necklace"></div>
  <div class="abs brand">HARPER<br>LORETTA</div>
  <div class="abs call">
    <svg width="20" height="20" viewBox="0 0 24 24"><path fill="#fff" d="M6.6 10.8a15 15 0 0 0 6.6 6.6l2.2-2.2c.3-.3.7-.4 1-.2 1.1.4 2.3.6 3.6.6.6 0 1 .4 1 1V20c0 .6-.4 1-1 1A17 17 0 0 1 3 4c0-.6.4-1 1-1h3.5c.6 0 1 .4 1 1 0 1.3.2 2.5.6 3.6.1.3 0 .7-.2 1z"/></svg>
    <span>Call <b>(555) 014-2288</b></span>
  </div>
  <span class="abs btn donate-top">Donate Now</span>
  <nav class="abs nav">
    <span class="active">Home</span><span>Biography</span><span>Events</span><span>Endorsements</span><span>Voting Information</span><span>Contact</span>
  </nav>
  <h1 class="abs hero-title">Judge<br>Harper<br>Loretta</h1>
  <span class="abs btn read-more">Read More</span>
  <div class="abs arrow" style="left:63px;top:318px"><svg width="30" height="30" viewBox="0 0 30 30"><path d="M17 9l-6 6 6 6" fill="none" stroke="#fff" stroke-width="2.4"/></svg></div>
  <div class="abs arrow" style="left:1106px;top:318px"><svg width="30" height="30" viewBox="0 0 30 30"><path d="M13 9l6 6-6 6" fill="none" stroke="#fff" stroke-width="2.4"/></svg></div>
  <svg class="abs hero-wave" viewBox="0 0 1200 180" preserveAspectRatio="none">
    <path d="M0,150 C180,60 330,30 520,50 C560,54 600,58 640,62 L1200,150 L1200,180 L0,180Z" fill="var(--blue)"/>
    <path d="M0,180 C200,80 360,55 560,62 C800,70 1000,130 1200,136 L1200,180Z" fill="#fff"/>
  </svg>
</section>

<!-- About -->
<div class="abs about-photo" role="img" aria-label="Photo of the candidate with her husband outdoors"></div>
<div class="abs about-kicker">About</div>
<div class="abs about-name">Harper Loretta</div>
<p class="abs about-text">My candidacy is based on the belief that the judiciary needs to be accountable to the citizens it serves. This starts with being present and accessible to ensure that both victims of crime, as well as those accused, have their day in court without unnecessary delays. Additionally, it is incumbent upon the judiciary to be proactive and innovative by starting programs that work to deter crime and reduce the recidivism rate. When elected, I will start a first time offenders program to help those accused of lower level felonies get an education</p>
<span class="abs btn about-btn">Read More</span>

<!-- Thanks band -->
<section class="abs band"></section>
<p class="abs thanks">Thank you Maple County for your support and votes!<br><b>Because of you, I am proud to say that I am the Democratic</b><br>Judge of the 318th Judicial District Court.</p>

<div class="abs feature" style="left:136px">
  <div class="icon"><svg width="60" height="60" viewBox="0 0 60 60" fill="none" stroke="#fff" stroke-width="2.4"><circle cx="34" cy="22" r="10"/><path d="M34 16v12M31 19h5a2 2 0 0 1 0 4h-4a2 2 0 0 0 0 4h5"/><path d="M6 42h10l8 4h12l14-8a3 3 0 0 0-3-4l-11 5H26"/><path d="M34 6V2M24 9l-3-3M44 9l3-3"/></svg></div>
  <h3>Donate</h3>
  <p>Sed ut perspiciatis unde omnis iste natus error sit voluptatem accusantium doloremque laudantium, totam rem aperiam, eaque ipsa quae ab illo inventore veritatis et quasi architecto</p>
</div>
<div class="abs feature" style="left:463px">
  <div class="icon"><svg width="60" height="60" viewBox="0 0 60 60" fill="none" stroke="#fff" stroke-width="2.4"><rect x="10" y="26" width="40" height="24" rx="2"/><path d="M10 34h40"/><path d="M20 26l10-16 12 8-6 8"/><circle cx="30" cy="42" r="5"/><path d="M27.5 42l2 2 3.5-4"/></svg></div>
  <h3>Voting Information</h3>
  <p>Sed ut perspiciatis unde omnis iste natus error sit voluptatem accusantium doloremque laudantium, totam rem aperiam, eaque ipsa quae ab illo inventore veritatis et quasi architecto</p>
</div>
<div class="abs feature" style="left:789px">
  <div class="icon"><svg width="60" height="60" viewBox="0 0 60 60" fill="none" stroke="#fff" stroke-width="2.4"><path d="M8 48l14-14 8 8 20-20"/><path d="M42 22h8v8"/><circle cx="24" cy="16" r="4"/><path d="M22 20l-6 10M24 22l8 6"/></svg></div>
  <h3>Endorsements</h3>
  <p>Sed ut perspiciatis unde omnis iste natus error sit voluptatem accusantium doloremque laudantium, totam rem aperiam, eaque ipsa quae ab illo inventore veritatis et quasi architecto</p>
</div>

<!-- Campaign video -->
<section class="abs lower-band"></section>
<h2 class="abs section-title" style="top:2025px">Loretta Harper Campaign</h2>
<div class="abs video" role="img" aria-label="Video still of a city skyline at dusk with a lit green tower"></div>
<div class="abs play"><svg width="20" height="22" viewBox="0 0 20 22"><path d="M2 1l17 10L2 21z" fill="#fff"/></svg></div>

<!-- Blog -->
<h2 class="abs section-title" style="top:2639px">Latest Blog</h2>
<div class="abs post-main" role="img" aria-label="Photo of the candidate in a dark suit in front of the bridge"></div>
<div class="abs post-overlay">
  <h4>Nemo enim ipsam voluptatem<br>quia voluptas</h4>
  <div class="meta"><span>Jan 25, 2019</span><span class="sep" style="background:#fff"></span><span>2 comments</span></div>
  <p>Sed ut perspiciatis unde omnis iste natus error sit vuptatem accusantium doloremque</p>
</div>
<article class="abs post" style="top:2733px">
  <div class="thumb" role="img" aria-label="Photo of a hand dropping a ballot into a box with flags behind" style="background:linear-gradient(135deg,#1c2a55 0%,#c9cfd8 55%,#8a8f99 100%)"></div>
  <div class="body">
    <h4>Nemo enim ipsam volupta</h4>
    <div class="meta"><span>Jan 25, 2019</span><span class="sep"></span><span>2 comments</span></div>
    <p>Sed ut perspiciatis unde omnis iste natus error sit vuptatem aum doloremque</p>
  </div>
</article>
<article class="abs post" style="top:2925px">
  <div class="thumb" role="img" aria-label="Photo of voting stickers with stars and stripes" style="background:linear-gradient(135deg,#c8283a 0%,#f3f3f3 45%,#21396e 100%)"></div>
  <div class="body">
    <h4>Nemo enim ipsam volupta</h4>
    <div class="meta"><span>Jan 25, 2019</span><span class="sep"></span><span>2 comments</span></div>
    <p>Sed ut perspiciatis unde omnis iste natus error sit vuptatem aum doloremque</p>
  </div>
</article>

<!-- Testimonials -->
<h2 class="abs section-title" style="top:3252px">Our Clients Says</h2>
<div class="abs quote" style="left:143px">
  <div class="stars"><svg width="82" height="14" viewBox="0 0 82 14"><g fill="#e53935"><rect x="0" y="0" width="14" height="14" rx="2"/><rect x="17" y="0" width="14" height="14" rx="2"/><rect x="34" y="0" width="14" height="14" rx="2"/><rect x="51" y="0" width="14" height="14" rx="2"/><rect x="68" y="0" width="14" height="14" rx="2"/></g></svg></div>
  <p><span>“</span>Sed ut perspiciatis unde omnis iste natus error sit voluptatem accusam dolemque laudantium, totam rem apm, eaque ipsa quae ab illo</p>
</div>
<div class="abs quote" style="left:461px">
  <div class="stars"><svg width="82" height="14" viewBox="0 0 82 14"><g fill="#e53935"><rect x="0" y="0" width="14" height="14" rx="2"/><rect x="17" y="0" width="14" height="14" rx="2"/><rect x="34" y="0" width="14" height="14" rx="2"/><rect x="51" y="0" width="14" height="14" rx="2"/><rect x="68" y="0" width="14" height="14" rx="2"/></g></svg></div>
  <p><span>“</span>Sed ut perspiciatis unde omnis iste natus error sit voluptatem accusam dolemque laudantium, totam rem apm, eaque ipsa quae ab illo</p>
</div>
<div class="abs quote" style="left:779px">
  <div class="stars"><svg width="82" height="14" viewBox="0 0 82 14"><g fill="#e53935"><rect x="0" y="0" width="14" height="14" rx="2"/><rect x="17" y="0" width="14" height="14" rx="2"/><rect x="34" y="0" width="14" height="14" rx="2"/><rect x="51" y="0" width="14" height="14" rx="2"/><rect x="68" y="0" width="14" height="14" rx="2"/></g></svg></div>
  <p><span>“</span>Sed ut perspiciatis unde omnis iste natus error sit voluptatem accusam dolemque laudantium, totam rem apm, eaque ipsa quae ab illo</p>
</div>
<div class="abs author" style="left:151px"><div class="avatar" role="img" aria-label="Reviewer photo"></div><div><div class="name">Ana L Brooks</div><div class="date">5/01/2019</div></div></div>
<div class="abs author" style="left:469px"><div class="avatar" role="img" aria-label="Reviewer photo"></div><div><div class="name">Ana L Brooks</div><div class="date">5/01/2019</div></div></div>
<div class="abs author" style="left:787px"><div class="avatar" role="img" aria-label="Reviewer photo"></div><div><div class="name">Ana L Brooks</div><div class="date">5/01/2019</div></div></div>
<div class="abs dots"><i></i><i></i><i class="on"></i><i></i><i></i></div>

<!-- Contact -->
<div class="abs contact-bg" role="img" aria-label="Faint city skyline over blue"></div>
<svg class="abs contact" viewBox="0 0 1200 680" preserveAspectRatio="none">
  <path d="M0,80 C300,30 600,150 900,120 C1050,105 1140,60 1200,70 L1200,110 L0,110Z" fill="var(--blue)"/>
  <path d="M700,140 C900,150 1080,90 1200,0 L1200,40 C1090,110 930,160 700,140Z" fill="var(--orange)"/>
</svg>
<h2 class="abs section-title contact-title">Contact Us</h2>
<div class="abs info" style="left:150px">
  <div class="ic"><svg width="18" height="22" viewBox="0 0 18 22"><path d="M9 1a7 7 0 0 0-7 7c0 5 7 13 7 13s7-8 7-13a7 7 0 0 0-7-7z" fill="none" stroke="#fff" stroke-width="2"/><circle cx="9" cy="8" r="2.5" fill="#fff"/></svg></div>
  <div><b>Address:</b><br><span style="font-size:16px">PO Box 40217 Fairview,<br>Texas 75000</span></div>
</div>
<div class="abs info" style="left:448px">
  <div class="ic"><svg width="20" height="20" viewBox="0 0 24 24"><path fill="#fff" d="M6.6 10.8a15 15 0 0 0 6.6 6.6l2.2-2.2c.3-.3.7-.4 1-.2 1.1.4 2.3.6 3.6.6.6 0 1 .4 1 1V20c0 .6-.4 1-1 1A17 17 0 0 1 3 4c0-.6.4-1 1-1h3.5c.6 0 1 .4 1 1 0 1.3.2 2.5.6 3.6.1.3 0 .7-.2 1z"/></svg></div>
  <div><b>Phone:</b><br>(555) 014-2288</div>
</div>
<div class="abs info" style="left:694px">
  <div class="ic"><svg width="20" height="16" viewBox="0 0 20 16"><rect x="1" y="1" width="18" height="14" rx="2" fill="none" stroke="#fff" stroke-width="2"/><path d="M1 2l9 7 9-7" fill="none" stroke="#fff" stroke-width="2"/></svg></div>
  <div><b>Email:</b><br><b style="font-size:19px">lorettaforjudge318@example.com</b></div>
</div>
<div class="abs field" style="left:158px;top:3990px;width:424px;height:40px">Name *</div>
<div class="abs field" style="left:158px;top:4045px;width:424px;height:40px">Phone *</div>
<div class="abs field" style="left:158px;top:4098px;width:424px;height:40px">Subject *</div>
<div class="abs field area" style="left:606px;top:3990px;width:424px;height:150px">Message</div>
<span class="abs btn submit">Submit</span>

<!-- Footer -->
<p class="abs footer-text">Harper Loretta © 2019 All Rights Reserved | Privacy Policy</p>
<span class="abs social" style="left:533px" aria-label="Social link"></span>
<span class="abs social" style="left:582px" aria-label="Social link"></span>
<span class="abs social" style="left:630px" aria-label="Social link"></span>

</body>
</html>
```